Passionate Homecare Agency Needs an "Employee News" Webpage Design

We are a homecare agency with more than 300 employees who provide personal care and assistance with the activities of daily living in clients’ homes. Our company slogan is “Someone you can depend on… Without question.” We strive to provide our clients with the highest quality, compassionate care possible, and we want our employees to feel inspired to do just that.

We are looking for an employee web page design to add to our existing website that makes our field employees feel connected to the company, is fun and energetic, and provides our caregivers with helpful information, employee news, and recognition. We want this to be a hub for communication and celebration, and also showcase our appreciation for all that they do!

We look forward to your designs! The sky's the limit!
Updates

Reason: Looking for a few more designs that fit our descriptions before making a final decision.

Target Market(s)

Our Employees

Industry/Entity Type

Home Health Care

Number of Pages Required

1 page

Colors

Designer to choose colors to be used in the design.

Requirements
Must have
• We would like to have sections like:
• -Employee of the Month/Week
• -Caregiver Tips and Tricks
• -Birthdays and Anniversaries
• -New Employees
• -Area to add links to our social media (Facebook, Instagram, Twitter)
• -etc!
Nice to have
• Bright colors and fun themes.

```html
<!DOCTYPE html>
<html lang="en">
<head>
<meta charset="utf-8">
<title>Hartwell Care Group – Employee News</title>
<link rel="stylesheet" href="https://fonts.googleapis.com/css2?family=Oswald:wght@600&family=Cormorant+Garamond:wght@500;700&family=Open+Sans:ital,wght@0,400;0,600;1,400&display=swap">
<style>
:root{
  --teal:#3a8aa0;
  --teal-dark:#2f7487;
  --salmon:#f5957a;
  --salmon-band:#f6a184;
  --blush:#fbe7de;
  --ink:#222;
  --grey-text:#8a8a8a;
  --card:#f0f0f0;
  --panel:#4a3128;
  --footer:#141414;
  --white:#fff;
}
*{box-sizing:border-box;margin:0;padding:0}
html,body{width:1200px;height:3462px;overflow:hidden}
body{position:relative;background:var(--white);font-family:"Open Sans",Arial,sans-serif;color:var(--ink)}
.abs{position:absolute}
.section-title{font-family:"Cormorant Garamond",Georgia,serif;font-weight:500;color:var(--teal);font-size:46px;letter-spacing:1px;text-align:center;position:absolute;left:0;width:1200px}
.btn{position:absolute;background:var(--salmon);color:var(--white);font-family:"Cormorant Garamond",Georgia,serif;font-weight:700;font-size:21px;letter-spacing:1px;display:flex;align-items:center;justify-content:center}

/* header */
.site-header{position:absolute;left:0;top:0;width:1200px;height:148px;background:var(--white)}
.brand{position:absolute;left:76px;top:52px;font-family:"Cormorant Garamond",Georgia,serif;font-weight:700;font-size:34px;color:var(--ink);display:flex;align-items:center;gap:10px}
.brand .dot{width:18px;height:18px;border-radius:50%;background:var(--ink)}
.call{position:absolute;left:900px;top:18px;display:flex;gap:12px}
.call small{display:block;font-family:"Cormorant Garamond",Georgia,serif;font-size:16px;color:#777}
.call strong{font-size:24px;color:var(--teal);font-weight:600}
.nav{position:absolute;top:95px;left:420px;display:flex;height:48px}
.nav a{display:flex;align-items:center;padding:0 14px;font-size:15px;color:var(--ink);text-decoration:none;letter-spacing:.3px}
.nav a.active{background:var(--salmon);color:var(--white)}

/* hero */
.hero{position:absolute;left:0;top:148px;width:1200px;height:530px;background:linear-gradient(100deg,#c9b6a2 0%,#d9c9b6 35%,#b79d87 60%,#e6ddd0 100%)}
.hero h1{position:absolute;right:74px;top:110px;font-family:Oswald,Impact,sans-serif;font-weight:600;font-size:82px;line-height:88px;color:var(--white);text-align:right;text-transform:uppercase;text-shadow:0 2px 4px rgba(0,0,0,.35)}
.hero p{position:absolute;right:74px;top:300px;font-family:"Cormorant Garamond",Georgia,serif;font-weight:700;font-size:30px;color:var(--white);text-shadow:0 1px 3px rgba(0,0,0,.4)}
.arrow{position:absolute;top:220px}
.brand-card{position:absolute;top:447px;height:157px;background:#f4f4f4;border:9px solid var(--teal);display:flex;align-items:center;justify-content:center;font-family:"Cormorant Garamond",Georgia,serif;font-weight:700;font-size:40px}
.brand-card.home{left:78px;width:517px;color:var(--teal)}
.brand-card.senior{left:605px;width:517px;border-color:var(--salmon);color:var(--teal)}

/* tips */
.tips-photo{position:absolute;left:46px;top:785px;width:427px;height:468px;background:radial-gradient(ellipse at 50% 60%,#5fc3dc 0%,#8fd3e4 40%,#fff 72%)}
.tips h2{position:absolute;left:498px;top:818px;font-family:"Cormorant Garamond",Georgia,serif;font-weight:500;font-size:45px;color:var(--teal);letter-spacing:1px}
.tips p{position:absolute;left:500px;width:625px;font-size:13.5px;line-height:25px;color:var(--grey-text)}

/* employee of month */
.eotm{position:absolute;left:0;top:1253px;width:1200px;height:605px;background:linear-gradient(135deg,#f4a88d,#f29a7e 50%,#f3a78c)}
.eotm-head{position:absolute;left:78px;top:134px;width:1044px;height:60px;background:var(--teal);color:var(--white);font-size:17px;display:flex;align-items:center}
.eotm-head span{padding-left:20px}
.names{position:absolute;left:78px;top:194px;width:296px}
.names li{list-style:none;height:58px;display:flex;align-items:center;padding-left:15px;font-family:"Cormorant Garamond",Georgia,serif;font-weight:500;font-size:19px;color:var(--ink);background:var(--blush);border-top:1px solid rgba(0,0,0,.05)}
.names li:nth-child(even){background:var(--teal);color:var(--white)}
.names li.current{position:relative;background:#fff}
.detail{position:absolute;left:374px;top:194px;width:748px;height:346px;background:rgba(70,45,35,.88)}
.emp-photo{position:absolute;left:44px;top:23px;width:177px;height:175px;border:3px solid #fff;background:linear-gradient(180deg,#d8cfc8,#7fb1cf)}
.emp-name{position:absolute;left:0;width:265px;text-align:center;top:220px;font-family:"Cormorant Garamond",Georgia,serif;font-size:26px;color:var(--salmon)}
.emp-mail{position:absolute;left:0;width:265px;text-align:center;top:255px;font-family:"Cormorant Garamond",Georgia,serif;font-size:15px;color:#e8dcd5}
.emp-social{position:absolute;left:82px;top:286px;display:flex;gap:20px}
.emp-social i{display:block;width:20px;height:20px;border-radius:50%;background:var(--salmon)}
.detail p{position:absolute;left:249px;top:18px;width:460px;font-size:13px;line-height:26.5px;color:#f3e7e0}
.detail .contact{left:249px;top:254px;width:199px;height:56px}
.scroll{position:absolute;right:12px;top:10px;width:5px;height:326px;background:#fff;border-radius:3px}

/* celebration */
.sub{position:absolute;left:0;width:1200px;text-align:center;font-family:"Cormorant Garamond",Georgia,serif;font-size:16px;letter-spacing:1px;color:#444}
.celebrate{position:absolute;height:206px;background:var(--card)}
.celebrate .pic{position:absolute;left:0;top:0;width:219px;height:206px}
.celebrate h3{position:absolute;left:245px;top:30px;font-family:"Cormorant Garamond",Georgia,serif;font-weight:700;font-size:20px;color:var(--teal);letter-spacing:1px}
.celebrate p{position:absolute;left:245px;top:66px;width:250px;font-size:13.5px;line-height:27px;color:var(--grey-text)}
.celebrate a{position:absolute;left:245px;top:150px;font-family:"Cormorant Garamond",Georgia,serif;font-weight:700;font-size:14px;color:var(--salmon);text-decoration:none;letter-spacing:1px}

/* new employees */
.join{position:absolute;left:0;top:2527px;width:1200px;height:542px;background:linear-gradient(90deg,#f6a385,#f8ad90 50%,#f6a385)}
.join .lead{position:absolute;left:0;width:1200px;top:122px;text-align:center;font-style:italic;font-size:16px;color:var(--white)}
.join .register{position:absolute;left:0;width:1200px;top:165px;text-align:center;font-family:"Cormorant Garamond",Georgia,serif;font-weight:700;font-size:20px;color:var(--ink)}
.field{position:absolute;height:55px;background:rgba(255,255,255,.35);font-size:14px;color:#444;display:flex;align-items:center;padding-left:14px}
.apply{position:absolute;left:505px;top:422px;width:187px;height:53px;border:1px solid #fff;color:var(--white);font-family:"Cormorant Garamond",Georgia,serif;font-weight:700;font-size:21px;letter-spacing:1px;display:flex;align-items:center;justify-content:center}

/* call strip */
.tagline{position:absolute;left:150px;top:3144px;font-style:italic;font-size:25px;color:var(--ink)}
.call-btn{position:absolute;left:718px;top:3132px;width:341px;height:57px;background:var(--salmon);color:var(--white);display:flex;align-items:center;justify-content:center;gap:12px;font-size:22px;font-weight:600}
.call-btn em{font-family:"Cormorant Garamond",Georgia,serif;font-style:normal;font-weight:700}

/* footer */
.site-footer{position:absolute;left:0;top:3254px;width:1200px;height:208px;background:var(--footer);color:#ccc}
.foot-links{position:absolute;left:78px;top:50px;font-size:13px;color:#ddd}
.foot-links span{margin:0 10px;color:#888}
.copy{position:absolute;left:78px;top:80px;font-size:13px;color:#ddd}
.foot-social{position:absolute;left:78px;top:118px;display:flex;gap:17px}
.foot-social i{display:flex;align-items:center;justify-content:center;width:46px;height:46px;border-radius:6px;background:var(--salmon)}
.foot-social i::after{content:"";width:16px;height:16px;border-radius:50%;background:#fff}
.foot-brands{position:absolute;left:690px;top:82px;display:flex;gap:30px;font-family:"Cormorant Garamond",Georgia,serif;font-weight:700;font-size:30px;color:var(--white)}
</style>
</head>
<body>

<header class="site-header">
  <div class="brand"><span class="dot"></span>Hartwell</div>
  <div class="call">
    <svg width="46" height="46" viewBox="0 0 24 24"><path fill="#3a8aa0" d="M6.6 10.8a15 15 0 0 0 6.6 6.6l2.2-2.2c.3-.3.7-.4 1-.2 1.1.4 2.3.6 3.6.6.6 0 1 .4 1 1V20c0 .6-.4 1-1 1A17 17 0 0 1 3 4c0-.6.4-1 1-1h3.5c.6 0 1 .4 1 1 0 1.3.2 2.5.6 3.6.1.3 0 .7-.2 1z"/></svg>
    <div><small>Call Us On:</small><strong>555 - 014 - 2020</strong></div>
  </div>
  <nav class="nav">
    <a>HOME</a><a>OPEN SHIFT</a><a class="active">EMPLOYEE NEWS</a><a>MY SKILLS</a><a>EMPLOYMEE FORMS</a>
  </nav>
</header>

<section class="hero">
  <div class="abs" role="img" aria-label="Photo of a young caregiver kneeling beside a smiling senior woman in a wheelchair" style="left:0;top:0;width:700px;height:530px;background:linear-gradient(90deg,#d6c2b0,#c9ad97 60%,rgba(201,173,151,0))"></div>
  <svg class="arrow" style="left:28px" width="22" height="60" viewBox="0 0 22 60"><path d="M18 4 4 30l14 26" fill="none" stroke="#fff" stroke-width="3"/></svg>
  <svg class="arrow" style="right:28px" width="22" height="60" viewBox="0 0 22 60"><path d="M4 4l14 26L4 56" fill="none" stroke="#fff" stroke-width="3"/></svg>
  <h1>Someone you can<br>depend on</h1>
  <p>WITHOUT QUESTION</p>
  <div class="brand-card home">Hartwell Homecare</div>
  <div class="brand-card senior">Hartwell Senior Living</div>
</section>

<section class="tips">
  <div class="tips-photo" role="img" aria-label="Photo of a smiling nurse in blue scrubs with a stethoscope"></div>
  <h2>CAREGIVER TIPS AND TRICKS</h2>
  <p style="top:890px">Caregivers, CNAs and Nurse Aides work in the client's home providing personal care, companionship, running errands, assisting with the activities of daily living, and any and all duties related to homecare. Tasks include but are not limited to bathing, dressing, grooming, transferring, range of motion exercises, assisting ambulation with a wheelchair, walker, or cane, incontinence care, toileting, taking vital signs, housekeeping, meal preparation, daily paperwork / charting.</p>
  <p style="top:1045px">Minimum 3 months' hands-on personal caregiving experience with the activities of daily living, Current First Aid Certification.</p>
  <div class="btn" style="left:503px;top:1133px;width:180px;height:58px">KNOW MORE</div>
</section>

<section class="eotm" aria-label="Employee of the month">
  <div class="section-title" style="top:56px">EMPLOYEE OF THE MONTH/WEEK</div>
  <div class="eotm-head"><span style="width:296px">EMPLOYEE NAME</span><span>EMPLOYEE DETAIL</span></div>
  <ul class="names">
    <li class="current">Employee Name</li>
    <li>Employee Name 1</li>
    <li>Employee Name 2</li>
    <li>Employee Name 3</li>
    <li>Employee Name 4</li>
    <li>Employee Name 5</li>
  </ul>
  <svg class="abs" style="left:370px;top:194px" width="16" height="58" viewBox="0 0 16 58"><path d="M0 0h2l12 29L2 58H0z" fill="#fff"/></svg>
  <div class="detail">
    <div class="emp-photo" role="img" aria-label="Portrait photo of the featured employee"></div>
    <div class="emp-name">Employee Name</div>
    <div class="emp-mail">teamhub.example</div>
    <div class="emp-social"><i></i><i></i><i></i></div>
    <p>Lorem Ipsum is simply dummy text of the printing and typesetting industry. Lorem Ipsum has been the industry's standard dummy text ever since the 1500s, when an unknown printer took a galley of type and scrambled it to make a type specimen book. It has survived not only five centuries, but also the leap into electronic typesetting, remaining essentially unchanged. It was popularised in the 1960s with the release of Letraset sheets containing Lorem Ipsum passages, and more recently with desktop publishing software.</p>
    <div class="btn contact">CONTACT NOW</div>
    <div class="scroll"></div>
  </div>
</section>

<section class="celebration">
  <div class="section-title" style="top:1912px">OUR CELEBRATION</div>
  <div class="sub" style="top:1972px">EMPLOYMENT NEWS</div>

  <article class="celebrate" style="left:78px;top:2026px;width:517px">
    <div class="pic" role="img" aria-label="Photo of residents celebrating a birthday with cake" style="background:linear-gradient(135deg,#7a3b2e,#c9785d 60%,#e6b08e)"></div>
    <h3>BIRTHDAYS</h3>
    <p>Lorem Ipsum is simply dummy text of the printing and typesetting industry. Lorem Ipsum has been the.</p>
    <a>READMORE... »</a>
  </article>
  <article class="celebrate" style="left:612px;top:2026px;width:510px">
    <div class="pic" role="img" aria-label="Photo of a resident in a costume at a birthday party" style="background:linear-gradient(135deg,#3b3a6e,#8a4f8f 55%,#4e8a5a)"></div>
    <h3>BIRTHDAYS</h3>
    <p>Lorem Ipsum is simply dummy text of the printing and typesetting industry. Lorem Ipsum has been the.</p>
    <a>READMORE... »</a>
  </article>
  <article class="celebrate" style="left:78px;top:2262px;width:517px">
    <div class="pic" role="img" aria-label="Photo of seniors at an anniversary party with red balloons" style="background:linear-gradient(135deg,#b3232a,#d24a4a 50%,#8a6a5a)"></div>
    <h3>ANNIVERSARIES</h3>
    <p>Lorem Ipsum is simply dummy text of the printing and typesetting industry. Lorem Ipsum has been the.</p>
    <a>READMORE... »</a>
  </article>
  <article class="celebrate" style="left:612px;top:2262px;width:510px">
    <div class="pic" role="img" aria-label="Photo of an anniversary gathering in a decorated hall" style="background:linear-gradient(135deg,#6b5545,#a8897a 55%,#5a4638)"></div>
    <h3>ANNIVERSARIES</h3>
    <p>Lorem Ipsum is simply dummy text of the printing and typesetting industry. Lorem Ipsum has been the.</p>
    <a>READMORE... »</a>
  </article>
</section>

<section class="join" role="img" aria-label="Background collage of smiling employee photos under a peach tint">
  <div class="section-title" style="top:60px">NEW EMPLOYEES</div>
  <div class="lead">If a profession in home care sounds interesting to you, please apply online below!</div>
  <div class="register">REGISTER NOW !</div>
  <div class="field" style="left:238px;top:215px;width:357px">Name*</div>
  <div class="field" style="left:604px;top:215px;width:354px">Email*</div>
  <div class="field" style="left:238px;top:281px;width:357px">Phone*</div>
  <div class="field" style="left:604px;top:281px;width:354px">Resume*
    <svg class="abs" style="right:14px;top:18px" width="18" height="18" viewBox="0 0 24 24"><path d="M10 14a5 5 0 0 0 7 0l3-3a5 5 0 0 0-7-7l-1 1M14 10a5 5 0 0 0-7 0l-3 3a5 5 0 0 0 7 7l1-1" fill="none" stroke="#333" stroke-width="2.4"/></svg>
  </div>
  <div class="field" style="left:238px;top:348px;width:720px">List any training, certifications, etc applicable to position:</div>
  <div class="apply">APPLY NOW</div>
</section>

<div class="tagline">You're at home and we're there to simple help.</div>
<div class="call-btn"><em>Call Us</em>
  <svg width="36" height="36" viewBox="0 0 36 36"><circle cx="18" cy="18" r="18" fill="#3a8aa0"/><path transform="translate(8 8) scale(.85)" fill="#fff" d="M6.6 10.8a15 15 0 0 0 6.6 6.6l2.2-2.2c.3-.3.7-.4 1-.2 1.1.4 2.3.6 3.6.6.6 0 1 .4 1 1V20c0 .6-.4 1-1 1A17 17 0 0 1 3 4c0-.6.4-1 1-1h3.5c.6 0 1 .4 1 1 0 1.3.2 2.5.6 3.6.1.3 0 .7-.2 1z"/></svg>
  555 - 014 - 2020</div>

<footer class="site-footer">
  <div class="foot-links">Home<span>|</span>Open Shift<span>|</span>Employee News<span>|</span>My Skills<span>|</span>Employee Forms</div>
  <div class="copy">©Hartwell home care -2017 All rights reserved.</div>
  <div class="foot-social"><i></i><i></i><i></i></div>
  <div class="foot-brands"><span>Hartwell</span><span>Hartwell</span><span>Hartwell</span></div>
</footer>

</body>
</html>
```